Flyer for American Indian Elders on Dementia Warning Signs

We need a flyer designed for older adults who are American Indian or Alaska Native (in the U.S.).

Ideally, the flyer should complement the colors of our logos. The project logo and our organization logo are attached to the brief.

When people see the flyer we want them to feel that it represents their culture, is warm, and professional but relatable to older adults and people who have limited incomes.

I have attached an earlier draft of the document we designed ourselves BUT we want different and better.

It is for older adults who have trouble reading so:
1. you must use a font that is 11.5 points or larger
2. Do not put text over complex pictures or use shading with words
3. You can use a serif font for the heading, but should use san serif for the body text
4. There should be good contrast between the font color and background

Please do not use any images that include a head dress or pictures of American Indian people or things that are very traditional or "token" imagery.

We need to save a small space under the call out box/ somewhere on the flyer for other people to add their logo once they download.

Let us know if you have questions or need additional information.

Target Market(s)

Older American Indian people

Font styles to use
Serif
Sans Serif

Requirements
Must have
• Easy to read for older adults
Should not have
• indian headdress

```html
<!DOCTYPE html>
<html lang="en">
<head>
<meta charset="utf-8">
<title>10 Signs of Thinking or Memory Changes</title>
<link rel="stylesheet" href="https://fonts.googleapis.com/css2?family=Montserrat:wght@500;600;700&family=Roboto+Condensed:wght@300;400;700&display=swap">
<style>
:root{
  --teal:#4ea8b0;
  --teal-dark:#3d8b91;
  --maroon:#7d3a34;
  --maroon-deep:#6c302b;
  --grey:#d7d7d7;
  --grey-soft:#e6e6e6;
  --line:#b9b9b9;
  --ink:#222;
  --page:#f1f1f1;
  --white:#fff;
}
*{box-sizing:border-box;margin:0;padding:0}
html,body{width:783px;height:1200px;overflow:hidden;background:var(--page)}
body{font-family:"Montserrat",Arial,sans-serif;color:var(--ink)}
.flyer{position:absolute;left:11px;top:62px;width:760px;height:1076px;background:var(--white);box-shadow:0 2px 8px rgba(0,0,0,.12);overflow:hidden}

/* header */
.header{position:absolute;left:0;top:0;width:760px;height:137px;background:var(--grey)}
.brand{position:absolute;left:30px;top:34px;display:flex;align-items:center;gap:12px}
.brand-dot{width:70px;height:70px;border-radius:50%;background:var(--teal)}
.brand-name{font-family:"Roboto Condensed",Arial,sans-serif;font-weight:700;color:var(--teal);font-size:19px;line-height:1.05;text-transform:uppercase}
.title-panel{position:absolute;left:338px;top:0;width:422px;height:137px;background:var(--maroon);border-radius:0 0 0 18px}
.title{position:absolute;left:28px;top:22px;font-family:"Roboto Condensed",Arial,sans-serif;color:var(--white);text-transform:uppercase}
.title-num{position:absolute;left:0;top:-8px;font-size:76px;font-weight:700;line-height:1}
.title-l1{position:absolute;left:76px;top:2px;font-size:27px;font-weight:300;white-space:nowrap;line-height:1}
.title-l2{position:absolute;left:76px;top:30px;font-size:31px;font-weight:700;color:#5cc0c8;white-space:nowrap;line-height:1}
.title-l3{position:absolute;left:0;top:64px;font-size:31px;font-weight:400;white-space:nowrap;line-height:1}
.title-l3 b{font-weight:700}

/* signs column */
.signs{position:absolute;left:49px;top:158px;width:331px;height:895px;border:1px solid var(--line);border-left:1.5px solid var(--line)}
.signs::before,.signs::after{content:"";position:absolute;left:-4.5px;width:7px;height:7px;border-radius:50%;background:var(--maroon)}
.signs::before{top:-4px}
.signs::after{bottom:-4px}
.sign{position:absolute;left:24px;width:300px}
.sign-num{position:absolute;left:-38px;top:-3px;width:27px;height:27px;border-radius:50%;background:var(--white);border:2px solid var(--grey);display:flex;align-items:center;justify-content:center}
.sign-num span{width:19px;height:19px;border-radius:50%;background:var(--maroon);color:var(--white);font-size:10px;font-weight:700;display:flex;align-items:center;justify-content:center}
.sign-head{font-family:"Roboto Condensed",Arial,sans-serif;font-size:12.5px;line-height:14px;text-transform:uppercase;color:var(--teal);font-weight:700}
.sign-head .sub{color:var(--maroon);font-weight:400;display:block}
.sign-head .em{color:var(--maroon)}
.sign-list{list-style:none;margin-top:3px}
.sign-list li{position:relative;padding-left:22px;font-size:11px;font-weight:500;line-height:12px;margin-top:5px;width:258px}
.sign-list li::before{content:"";position:absolute;left:1px;top:1px;width:11px;height:11px;border-radius:50%;background:var(--maroon)}
.sign-list li::after{content:"";position:absolute;left:4.5px;top:3.5px;width:3px;height:5px;border:solid var(--white);border-width:0 1.5px 1.5px 0;transform:rotate(45deg)}
.sign-text{font-size:11px;font-weight:500;line-height:13px;margin-top:3px;width:268px}

/* right column */
.intro{position:absolute;left:420px;top:158px;width:300px;font-size:10.6px;font-weight:600;line-height:13.5px}
.intro p+p{margin-top:14px}
.notebook{position:absolute;left:420px;top:333px;width:306px;height:491px;border-radius:10px;overflow:hidden}
.note{position:relative;display:flex;align-items:center;padding-left:98px;padding-right:18px;color:var(--white);font-size:15px;font-weight:500;line-height:18px}
.note:nth-child(odd){background:var(--teal)}
.note:nth-child(even){background:var(--teal-dark)}
.note-icon{position:absolute;left:20px;top:50%;margin-top:-32px;width:64px;height:64px;border-radius:50%;background:var(--maroon);border:2px solid var(--white);box-shadow:0 0 0 3px rgba(255,255,255,.25)}
.note-icon svg{width:100%;height:100%}
.rings{position:absolute;left:420px;top:318px;width:306px;height:26px}
.logo-space{position:absolute;left:420px;top:841px;width:306px;height:68px;border-radius:12px;background:var(--grey-soft)}
.learn{position:absolute;left:420px;top:922px;width:160px;font-size:10.6px;font-weight:500;line-height:13px}
.visit{position:absolute;left:420px;top:994px;width:176px;height:20px;background:var(--teal);color:var(--white);font-weight:700;font-size:12px;letter-spacing:.4px;line-height:20px;padding-left:14px;clip-path:polygon(0 0,92% 0,100% 100%,0 100%)}
.partner{position:absolute;left:610px;top:930px;width:120px;display:flex;align-items:center;gap:6px}
.partner-mark{width:22px;height:22px;background:var(--teal);flex:none}
.partner-name{font-family:"Roboto Condensed",Arial,sans-serif;font-weight:700;color:var(--maroon);font-size:12.5px;line-height:13px;text-transform:uppercase}
.links{position:absolute;left:420px;top:1034px;display:flex;gap:10px;font-size:10.5px;font-weight:700}
.links span{display:flex;align-items:center;gap:4px}
.links svg{width:12px;height:12px}
.base-strip{position:absolute;left:0;bottom:0;width:760px;height:11px;background:var(--teal)}
</style>
</head>
<body>
<main class="flyer">

  <header class="header">
    <div class="brand">
      <div class="brand-dot"></div>
      <div class="brand-name">Native Elders<br>Brain Health<br>Center</div>
    </div>
    <div class="title-panel">
      <h1 class="title">
        <span class="title-num">10</span>
        <span class="title-l1">Signs of Thinking or</span>
        <span class="title-l2">Memory Changes</span>
        <span class="title-l3">That <b>Might Be Dementia</b></span>
      </h1>
    </div>
  </header>

  <section class="signs">
    <div class="sign" style="top:28px">
      <div class="sign-num"><span>1</span></div>
      <h2 class="sign-head">Memory loss that affects your daily life.<span class="sub">You may:</span></h2>
      <ul class="sign-list">
        <li>Forget events or important dates</li>
        <li>Repeat yourself</li>
        <li>Rely more often on lists or sticky notes to remember things</li>
      </ul>
    </div>
    <div class="sign" style="top:134px">
      <div class="sign-num"><span>2</span></div>
      <h2 class="sign-head">Trouble planning or solving problems<span class="sub">You may have a harder time:</span></h2>
      <ul class="sign-list">
        <li>Paying bills</li>
        <li>Cooking recipes you have used for years</li>
      </ul>
    </div>
    <div class="sign" style="top:212px">
      <div class="sign-num"><span>3</span></div>
      <h2 class="sign-head">Get confused about the time, date<br><span class="em">or where you are.</span></h2>
    </div>
    <div class="sign" style="top:253px">
      <div class="sign-num"><span>4</span></div>
      <h2 class="sign-head">Daily tasks are getting harder<span class="sub">Including:</span></h2>
      <ul class="sign-list">
        <li>Driving</li>
        <li>Making a grocery list or going shopping</li>
      </ul>
    </div>
    <div class="sign" style="top:332px">
      <div class="sign-num"><span>5</span></div>
      <h2 class="sign-head">Trouble with how your eyesight and thinking work together that gets worse.<span class="sub">This includes:</span></h2>
      <ul class="sign-list">
        <li>Tripping, falls, or problems with your balance</li>
        <li>Spilling or dropping things more</li>
      </ul>
    </div>
    <div class="sign" style="top:440px">
      <div class="sign-num"><span>6</span></div>
      <h2 class="sign-head">New trouble talking <span class="em">or writing</span></h2>
      <p class="sign-text">You have a hard time finding the words you want to say. For example, you may say “that thing on your wrist that tells time” instead of “watch.”</p>
    </div>
    <div class="sign" style="top:522px">
      <div class="sign-num"><span>7</span></div>
      <h2 class="sign-head">Lose and cannot find things.<span class="sub">For example, you:</span></h2>
      <ul class="sign-list">
        <li>Can’t find the coffee pot that you use every day</li>
        <li>Might put your car keys in the freezer</li>
      </ul>
    </div>
    <div class="sign" style="top:610px">
      <div class="sign-num"><span>8</span></div>
      <h2 class="sign-head">Notice changes in mood or personality<span class="sub">Such as being:</span></h2>
      <ul class="sign-list">
        <li>Easily mad or sad in everyday situations</li>
        <li>More fearful (scared) or suspicious (not trusting)</li>
      </ul>
    </div>
    <div class="sign" style="top:702px">
      <div class="sign-num"><span>9</span></div>
      <h2 class="sign-head">Act different and make poor choices<span class="sub">May make you more likely to:</span></h2>
      <ul class="sign-list">
        <li>Spend money you do not have or be a scam victim</li>
        <li>Stop washing up regularly or pay less attention to how you look</li>
        <li>Forget to take care of your pet</li>
      </ul>
    </div>
    <div class="sign" style="top:823px">
      <div class="sign-num"><span>10</span></div>
      <h2 class="sign-head">Pull away from friends and family<br><span class="em">Because it is harder to keep up.</span></h2>
      <p class="sign-text">You may not want to do things you used to enjoy, like sporting events, church, music, or sex.</p>
    </div>
  </section>

  <div class="intro">
    <p>As we get older, we may slow down a bit. This is a normal part of aging. Changes in memory or thinking that make it harder to get through the day, are not a normal part of aging. These may be early signs of dementia.</p>
    <p>Because American Indian and Alaska Native people have a high risk of dementia, it is important to know the warning signs. Do you have any of these 10 signs? If so, talk to your doctor.</p>
  </div>

  <div class="notebook">
    <div class="note" style="height:137px">
      <div class="note-icon"><svg viewBox="0 0 64 64"><path d="M32 18 L46 42 H18 Z" fill="none" stroke="#fff" stroke-width="2.5" stroke-linejoin="round"/><line x1="32" y1="26" x2="32" y2="35" stroke="#fff" stroke-width="2.5" stroke-linecap="round"/><circle cx="32" cy="38.5" r="1.5" fill="#fff"/></svg></div>
      American Indian and Alaska Native people have a high risk of dementia.
    </div>
    <div class="note" style="height:129px">
      <div class="note-icon"><svg viewBox="0 0 64 64"><circle cx="32" cy="32" r="13" fill="none" stroke="#fff" stroke-width="2.2"/><path d="M24 32 q4 -6 8 0 t8 0" fill="none" stroke="#fff" stroke-width="2.2" stroke-linecap="round"/></svg></div>
      Big changes in memory or thinking that make it hard to get through the day are not a normal part
    </div>
    <div class="note" style="height:120px">
      <div class="note-icon"><svg viewBox="0 0 64 64"><rect x="17" y="19" width="30" height="20" rx="4" fill="none" stroke="#fff" stroke-width="2.2"/><path d="M24 39 l-3 7 9 -7" fill="none" stroke="#fff" stroke-width="2.2" stroke-linejoin="round"/><circle cx="26" cy="29" r="1.6" fill="#fff"/><circle cx="32" cy="29" r="1.6" fill="#fff"/><circle cx="38" cy="29" r="1.6" fill="#fff"/></svg></div>
      People with one or more of these 10 signs should talk to their doctor to find
    </div>
    <div class="note" style="height:105px">
      <div class="note-icon"><svg viewBox="0 0 64 64"><rect x="21" y="18" width="22" height="28" rx="2" fill="none" stroke="#fff" stroke-width="2.2"/><rect x="27" y="15" width="10" height="6" rx="1.5" fill="#fff"/><path d="M26 33 l4 4 8 -8" fill="none" stroke="#fff" stroke-width="2.4" stroke-linecap="round" stroke-linejoin="round"/></svg></div>
      Early dementia diagnosis gives you a chance to get care and plan your future.
    </div>
  </div>

  <svg class="rings" viewBox="0 0 306 26" aria-hidden="true">
    <g fill="#333" stroke="#555" stroke-width="2">
      <g id="ring"><path d="M28 18 V6 a3 3 0 0 1 6 0 V14" fill="none"/><circle cx="28" cy="19" r="3.5" stroke="none"/></g>
      <use href="#ring" x="25"/><use href="#ring" x="50"/><use href="#ring" x="75"/><use href="#ring" x="100"/><use href="#ring" x="125"/><use href="#ring" x="150"/><use href="#ring" x="175"/><use href="#ring" x="200"/><use href="#ring" x="225"/><use href="#ring" x="250"/>
    </g>
  </svg>

  <div class="logo-space" aria-label="Space for a partner logo"></div>

  <p class="learn">To learn more about the warning signs of dementia in American Indian and Alaska Native people</p>
  <div class="visit">VISIT OUR WEBSITE</div>

  <div class="partner">
    <div class="partner-mark"></div>
    <div class="partner-name">Circle of Elders Aging Network</div>
  </div>

  <div class="links">
    <span><svg viewBox="0 0 12 12"><g fill="none" stroke="#7d3a34" stroke-width="1"><circle cx="6" cy="6" r="5"/><ellipse cx="6" cy="6" rx="2.2" ry="5"/><line x1="1" y1="6" x2="11" y2="6"/></g></svg>www.elderbrainwell.org</span>
    <span><svg viewBox="0 0 12 12"><g fill="none" stroke="#7d3a34" stroke-width="1"><circle cx="6" cy="6" r="5"/><ellipse cx="6" cy="6" rx="2.2" ry="5"/><line x1="1" y1="6" x2="11" y2="6"/></g></svg>www.agingwellhub.org</span>
  </div>

  <div class="base-strip"></div>
</main>
</body>
</html>
```